stationary for hygienic company

We need a stationary design for hygienic company which provides public high end sanitary products and high end public lavatory.
We need a fresh and clean style stationary
we want the following things:
* logo (redesigned in eps/vector)
* Letterhead (with company details)
* letterhead (without company details)
* Business card
* note block
* ballpoint
* etcetera (a complete package)

```html
<!DOCTYPE html>
<html lang="en">
<head>
<meta charset="utf-8">
<title>Purelane Stationery</title>
<link href="https://fonts.googleapis.com/css2?family=Open+Sans:wght@300;400;600&display=swap" rel="stylesheet">
<style>
  :root {
    --backdrop: #8a8a8a;
    --paper: #ffffff;
    --ink: #3a3a3a;
    --ink-soft: #8c8c8c;
    --brand-blue: #1fb3e8;
    --brand-magenta: #e0197d;
    --night: #1c1c1e;
  }
  * { box-sizing: border-box; margin: 0; padding: 0; }
  html, body { width: 1200px; height: 863px; overflow: hidden; }
  body {
    background: var(--backdrop);
    font-family: "Open Sans", Arial, sans-serif;
    color: var(--ink);
    position: relative;
  }
  .piece { position: absolute; box-shadow: 0 6px 18px rgba(0,0,0,.25); }

  /* Brand name lockup */
  .brand { display: flex; align-items: center; gap: 6px; }
  .brand-dot { width: 14px; height: 14px; border-radius: 50%; background: var(--brand-blue); flex: none; }
  .brand-name { font-weight: 400; font-size: 20px; color: var(--ink); letter-spacing: .2px; }
  .brand-tag { font-size: 7px; color: var(--ink-soft); letter-spacing: .6px; text-transform: uppercase; margin-top: 2px; }
  .on-dark .brand-name { color: #fff; }

  /* Business cards */
  .card { width: 240px; height: 140px; left: 60px; border-bottom: 10px solid var(--brand-blue); padding: 20px; display: flex; justify-content: space-between; }
  .card-front { top: 190px; background: var(--paper); }
  .card-back { top: 380px; background: var(--night); }
  .card-details { align-self: center; text-align: left; font-size: 7px; line-height: 1.7; color: var(--ink-soft); }
  .card-holder { font-size: 9px; font-weight: 600; color: var(--brand-blue); letter-spacing: 1px; text-transform: uppercase; margin-bottom: 4px; }

  /* Envelope */
  .envelope { left: 340px; top: 100px; width: 320px; height: 170px; background: var(--night); overflow: hidden; }
  .envelope svg { position: absolute; inset: 0; }

  /* Compliment slip */
  .slip { left: 340px; top: 300px; width: 320px; height: 170px; background: var(--paper); padding: 18px 20px; }
  .slip-rule { position: absolute; left: 150px; top: 0; bottom: 0; width: 1px; background: var(--brand-blue); }
  .slip-contact { margin-top: 10px; font-size: 6px; line-height: 1.7; color: var(--ink-soft); }

  /* Phone screen */
  .app-screen { left: 430px; top: 505px; width: 150px; height: 266px; background: var(--brand-blue); display: flex; flex-direction: column; align-items: center; }
  .app-brand { margin-top: 80px; }
  .app-brand .brand-name { color: #fff; font-size: 18px; }
  .app-brand .brand-dot { background: #fff; }
  .app-loader { margin-top: 40px; }
  .app-tabs { margin-top: auto; width: 100%; height: 30px; display: flex; justify-content: space-around; align-items: center; border-top: 1px solid rgba(255,255,255,.4); }

  /* Letterhead */
  .folder { left: 724px; top: 112px; width: 440px; height: 640px; background: var(--brand-blue); border-bottom: 4px solid var(--brand-magenta); }
  .letterhead { left: 710px; top: 96px; width: 440px; height: 640px; background: var(--paper); padding: 48px 56px; }
  .logo-frame { margin: 0 auto 34px; width: 116px; height: 76px; border: 1.5px solid var(--brand-blue); display: flex; flex-direction: column; align-items: center; justify-content: center; }
  .letter-body { font-size: 8.5px; line-height: 1.75; color: var(--ink-soft); }
  .letter-body p { margin-bottom: 10px; }
  .letter-contact { position: absolute; left: 56px; top: 430px; padding-left: 8px; border-left: 1px solid var(--brand-magenta); font-size: 6px; line-height: 1.8; color: var(--ink-soft); }
  .signature { position: absolute; left: 230px; top: 500px; font-size: 9px; color: var(--ink); }
  .signature span { display: block; font-size: 7px; color: var(--ink-soft); font-style: normal; }
</style>
</head>
<body>

  <!-- Business card, front -->
  <div class="piece card card-front">
    <div>
      <div class="brand"><span class="brand-dot"></span><span class="brand-name">Purelane</span></div>
      <div class="brand-tag">Hygiene Solutions</div>
    </div>
    <div class="card-details">
      <div class="card-holder">Noah Whitfield</div>
      555 014 2290<br>noah@purelane.com<br>www.purelane.com
    </div>
  </div>

  <!-- Business card, back -->
  <div class="piece card card-back on-dark">
    <div>
      <div class="brand"><span class="brand-dot"></span><span class="brand-name">Purelane</span></div>
      <div class="brand-tag">Hygiene Solutions</div>
    </div>
    <div class="card-details">
      <div class="card-holder">Noah Whitfield</div>
      555 014 2290<br>noah@purelane.com<br>www.purelane.com
    </div>
  </div>

  <!-- Envelope -->
  <div class="piece envelope">
    <svg width="320" height="170" viewBox="0 0 320 170">
      <polygon points="0,0 320,0 320,170 260,170" fill="#1fb3e8"/>
      <polygon points="0,0 320,0 300,150" fill="#2a2a2c"/>
    </svg>
  </div>

  <!-- Compliment slip -->
  <div class="piece slip">
    <div class="slip-rule"></div>
    <div class="brand"><span class="brand-dot"></span><span class="brand-name">Purelane</span></div>
    <div class="brand-tag">Hygiene Solutions</div>
    <div class="slip-contact">555 014 2290<br>hello@purelane.com<br>www.purelane.com</div>
  </div>

  <!-- App splash screen -->
  <div class="piece app-screen">
    <div class="app-brand">
      <div class="brand"><span class="brand-dot"></span><span class="brand-name">Purelane</span></div>
      <div class="brand-tag" style="color:#e8f7fd;text-align:center">Hygiene Solutions</div>
    </div>
    <svg class="app-loader" width="24" height="24" viewBox="0 0 24 24">
      <circle cx="12" cy="12" r="9" fill="none" stroke="rgba(255,255,255,.35)" stroke-width="2"/>
      <path d="M12 3 A9 9 0 0 1 21 12" fill="none" stroke="#fff" stroke-width="2"/>
    </svg>
    <div class="app-tabs">
      <svg width="10" height="10" viewBox="0 0 10 10"><path d="M1 9 L9 1 M5 1 H9 V5" stroke="#fff" fill="none"/></svg>
      <svg width="10" height="10" viewBox="0 0 10 10"><circle cx="5" cy="5" r="4" stroke="#fff" fill="none"/></svg>
      <svg width="10" height="10" viewBox="0 0 10 10"><path d="M5 1 C2 1 2 5 5 9 C8 5 8 1 5 1Z" stroke="#fff" fill="none"/></svg>
      <svg width="10" height="10" viewBox="0 0 10 10"><path d="M2 1 L4 1 L5 3 L4 4 C5 6 6 7 7 7 L8 6 L9 7 L9 9 C5 9 1 5 2 1Z" stroke="#fff" fill="none"/></svg>
    </div>
  </div>

  <!-- Folder and letterhead -->
  <div class="piece folder"></div>
  <div class="piece letterhead">
    <div class="logo-frame">
      <div class="brand"><span class="brand-dot"></span><span class="brand-name">Purelane</span></div>
      <div class="brand-tag">Hygiene Solutions</div>
    </div>
    <div class="letter-body">
      <p>Thank you for choosing our washroom solutions. Our team designs premium sanitary fixtures and public lavatories that stay clean, quiet and easy to maintain. Every installation is planned with care, from the first survey to the final inspection, so your visitors enjoy a fresh space every day.</p>
      <p>We look forward to working with you on the next project. Please contact our office with any questions about product ranges, service plans or delivery times.</p>
    </div>
    <div class="letter-contact">555 014 2290<br>hello@purelane.com<br>www.purelane.com</div>
    <div class="signature">Elias Brandt<span>Co-founder &amp; CEO</span></div>
  </div>

</body>
</html>
```